Author/ Speaker Business Card design

I need a business card designed that will go with the branding that is already on my book and website. I like clean and straightforward, but I am not opposed to something more 'innovative'.

Target Market(s)

Colleges and Universities, educational institutions

Industry/Entity Type

Education

Contact Information for Business Card

Standard size. It should be able to be printed on good quality white or ivory paper.

Font styles to use
Sans Serif

Colors
0355a3

Requirements
Must have
• There's a blue on my website. It should have some blue. My logo is at the top. It should have the logo incorporated somewhere on it. My name, Author | Speaker | Teacher | Trainer, my phone number (+31 64-207 5819), my email address (milo@theboldlearner.example), Social media icons (twitter, Instagram, LinkedIn) with the addresses (twitter @writermilofenwick, Instagram - theboldlearner, LinkedIn - theboldlearner) By they way, the website is www.theboldlearner.example. There is a photo of the book on the website. Also, my full name is Milo Fenwick
Nice to have
• Try to use the font that is on the website and book. Also, if you could get that blue, that would be great.
Should not have
• My photo

```html
<!DOCTYPE html>
<html lang="en">
<head>
<meta charset="utf-8">
<title>The Bold Learner – Business Card</title>
<link rel="stylesheet" href="https://fonts.googleapis.com/css2?family=Carlito:wght@400;700&display=swap">
<style>
  :root {
    --page-bg: #d9d9dc;
    --card-white: #ffffff;
    --brand-blue: #2f4f9c;
    --blue-light: #7188c0;
    --blue-deep: #2b4a96;
    --icon-tint: #a9badf;
    --text-light: #ffffff;
  }
  * { margin: 0; padding: 0; box-sizing: border-box; }
  html, body {
    width: 1200px;
    height: 1200px;
    overflow: hidden;
    background: var(--page-bg);
    font-family: "Carlito", "Calibri", sans-serif;
  }
  .canvas {
    width: 1200px;
    height: 1200px;
    display: flex;
    align-items: center;
    justify-content: center;
  }
  .business-card {
    position: relative;
    width: 560px;
    height: 980px;
    background: var(--card-white);
    overflow: hidden;
    box-shadow: 0 10px 30px rgba(0,0,0,0.18);
  }
  .card-wave {
    position: absolute;
    inset: 0;
    width: 100%;
    height: 100%;
  }
  .brand-lockup {
    position: absolute;
    top: 120px;
    left: 0;
    width: 100%;
    display: flex;
    align-items: center;
    justify-content: center;
    gap: 18px;
  }
  .brand-dot {
    width: 64px;
    height: 64px;
    border-radius: 50%;
    background: var(--brand-blue);
  }
  .brand-name {
    color: var(--brand-blue);
    font-weight: 700;
    font-size: 44px;
    line-height: 1;
    width: 210px;
  }
  .card-details {
    position: absolute;
    left: 86px;
    top: 520px;
    right: 30px;
    color: var(--text-light);
  }
  .person-name {
    font-size: 50px;
    font-weight: 400;
    letter-spacing: 1px;
    text-transform: uppercase;
    line-height: 1;
  }
  .person-roles {
    margin-top: 10px;
    font-size: 24px;
    line-height: 1;
  }
  .contact-group {
    list-style: none;
    margin-top: 44px;
  }
  .contact-group + .contact-group { margin-top: 26px; }
  .contact-item {
    display: flex;
    align-items: center;
    gap: 12px;
    font-size: 25px;
    line-height: 1.35;
  }
  .contact-icon {
    flex: none;
    width: 24px;
    height: 24px;
  }
</style>
</head>
<body>
<main class="canvas">
  <article class="business-card">
    <svg class="card-wave" viewBox="0 0 560 980" preserveAspectRatio="none" aria-hidden="true">
      <defs>
        <linearGradient id="panelGradient" x1="0" y1="0.3" x2="1" y2="0.6">
          <stop offset="0" stop-color="var(--blue-light)"/>
          <stop offset="0.45" stop-color="var(--brand-blue)"/>
          <stop offset="1" stop-color="var(--blue-deep)"/>
        </linearGradient>
      </defs>
      <path d="M0 350 Q 300 420 560 250 L560 980 L0 980 Z" fill="url(#panelGradient)"/>
      <path d="M40 340 Q 300 395 520 250" fill="none" stroke="var(--brand-blue)" stroke-width="3" stroke-linecap="round"/>
    </svg>

    <header class="brand-lockup">
      <span class="brand-dot"></span>
      <span class="brand-name">The Bold Learner</span>
    </header>

    <section class="card-details">
      <h1 class="person-name">Milo Fenwick</h1>
      <p class="person-roles">Author | Speaker | Teacher | Trainer</p>

      <ul class="contact-group">
        <li class="contact-item">
          <svg class="contact-icon" viewBox="0 0 24 24" aria-hidden="true">
            <rect width="24" height="24" rx="4" fill="var(--icon-tint)"/>
            <path d="M8 5l2.5 3-1.5 1.5c.8 1.8 2.2 3.2 4 4l1.5-1.5 3 2.5-1.5 2.5c-4.5-.3-9-4.8-9.3-9.3z" fill="var(--brand-blue)"/>
          </svg>
          <span>+31 64-207 5819</span>
        </li>
        <li class="contact-item">
          <svg class="contact-icon" viewBox="0 0 24 24" aria-hidden="true">
            <rect width="24" height="24" rx="4" fill="var(--icon-tint)"/>
            <rect x="5" y="7" width="14" height="10" fill="none" stroke="var(--brand-blue)" stroke-width="1.6"/>
            <path d="M5 7l7 6 7-6" fill="none" stroke="var(--brand-blue)" stroke-width="1.6"/>
          </svg>
          <span>milo@theboldlearner.example</span>
        </li>
      </ul>

      <ul class="contact-group">
        <li class="contact-item">
          <svg class="contact-icon" viewBox="0 0 24 24" aria-hidden="true"><rect width="24" height="24" rx="4" fill="var(--icon-tint)"/></svg>
          <span>@writermilofenwick</span>
        </li>
        <li class="contact-item">
          <svg class="contact-icon" viewBox="0 0 24 24" aria-hidden="true"><rect width="24" height="24" rx="4" fill="var(--icon-tint)"/></svg>
          <span>theboldlearner</span>
        </li>
      </ul>

      <ul class="contact-group">
        <li class="contact-item">
          <svg class="contact-icon" viewBox="0 0 24 24" aria-hidden="true"><rect width="24" height="24" rx="4" fill="var(--icon-tint)"/></svg>
          <span>theboldlearner</span>
        </li>
        <li class="contact-item">
          <svg class="contact-icon" viewBox="0 0 24 24" aria-hidden="true">
            <rect width="24" height="24" rx="4" fill="var(--icon-tint)"/>
            <circle cx="12" cy="12" r="6.5" fill="none" stroke="var(--brand-blue)" stroke-width="1.5"/>
            <path d="M5.5 12h13M12 5.5c-3 3.5-3 9.5 0 13M12 5.5c3 3.5 3 9.5 0 13" fill="none" stroke="var(--brand-blue)" stroke-width="1.2"/>
          </svg>
          <span>www.theboldlearner.example</span>
        </li>
      </ul>
    </section>
  </article>
</main>
</body>
</html>
```